Website on Hubspot CMS -Boutique consulting firm focused on the events and event tech industries

Design website for our business using Hubspot CMS. Some pages already done. We would like those tweaked to match your recommended design. We also would like landing pages created for four business services offerings. We have a color palette and logo.

Our current website can be found here: www.qlvadvisors.co

QLV Advisors has four service lines:
1. Outsourced Sales
2. Harbor Ledger Strategic Consulting
3. Gridweave Strategic Consulting
4. QLV VIP

Target Market(s)

event organizers, media companies, corporate event marketers, event tech organizations

Industry/Entity Type

Consulting

Coding

Coded - Design and coding required

Number of Pages Required

5+ page

Font styles to use
Sans Serif

Requirements
Must have
• This will be a website built using Hubspot CMS. If you are not familiar with this, please do not participate as we will not be able to use your designs.
SEO optimized
Landing pages with lead capture leading to content downloads
Each service line needs its own page/s with cta's
Highly visual, modern, bold
Navigational areas: Home, Services, Resources, Events, Blog, About Us
Content formats: video, podcasts, content downloads
Will need at least 4 landing pages in addition to the website for each service line plus templates in case we need to update with new copy
We have or own color palette and logo as well as logos for Harbor Ledger and Gridweave. Those colors must be used.
Font can be modified
We need to have a conversation with the designer that is chosen to go over each service line and also understand what kind of images we should be uploading.
Nice to have
• We would really like the site to reflect the following words:
Bold
Future focused
Results oriented
Hyper focused on the events and event technology sectors (sub sectors: corporate event marketers and B2B media companies).
Should not have
• Flat one page design

```html
<!DOCTYPE html>
<html lang="en">
<head>
<meta charset="utf-8">
<title>About Us – QLV Advisors</title>
<link rel="stylesheet" href="https://fonts.googleapis.com/css2?family=Montserrat:wght@400;500;600;700&family=Lato:ital,wght@0,400;0,700;1,400&display=swap">
<style>
:root{
  --orange:#f24f1c;
  --ink:#1f1f1f;
  --body:#5c5c5c;
  --grey-bg:#f4f4f4;
  --line:#d8d8d8;
  --dark:#2a2e35;
  --white:#fff;
}
*{box-sizing:border-box;margin:0;padding:0}
html,body{width:1200px;height:5093px;overflow:hidden}
body{position:relative;font-family:'Lato',sans-serif;color:var(--ink);background:var(--white)}
.abs{position:absolute}
.center{text-align:center}
.eyebrow{font-family:'Montserrat',sans-serif;font-weight:500;color:var(--orange);font-size:24px;letter-spacing:.5px;text-transform:uppercase;width:1200px;left:0;text-align:center}
.h2{font-family:'Montserrat',sans-serif;font-weight:700;font-size:40px;text-transform:uppercase;width:1200px;left:0;text-align:center;color:var(--ink)}
.copy{font-size:15px;line-height:26.5px;color:var(--body);text-align:center}
.btn{background:var(--orange);color:var(--white);font-family:'Montserrat',sans-serif;font-weight:600;text-transform:uppercase;display:flex;align-items:center;justify-content:center}

/* hero */
.hero{top:0;left:0;width:1200px;height:445px;background:linear-gradient(100deg,#1b2c44 0%,#2f4d6e 45%,#1c2a3d 75%,#0f1826 100%)}
.logo{left:110px;top:40px;color:var(--white);font-family:'Montserrat',sans-serif;font-weight:600;font-size:30px;display:flex;align-items:center;gap:10px}
.logo .mark{width:14px;height:14px;background:var(--white)}
.nav{top:50px;left:346px;display:flex;gap:30px;font-family:'Montserrat',sans-serif;font-size:15px;font-weight:500;color:var(--white);text-transform:uppercase}
.nav .active{color:var(--orange)}
.nav-cta{left:943px;top:32px;width:144px;height:55px;font-size:15px}
.hero-title{left:105px;top:228px;font-family:'Montserrat',sans-serif;font-weight:700;font-size:60px;line-height:72px;color:var(--white);white-space:nowrap}

/* values */
.value{width:260px;text-align:center}
.value .ring{width:166px;height:166px;margin:0 auto;border-radius:50%;border:3px solid #8a8a8a;display:flex;align-items:center;justify-content:center}
.value .ring-in{width:144px;height:144px;border-radius:50%;border:2px solid #cfcfcf;display:flex;align-items:center;justify-content:center}
.value p{margin-top:26px;font-family:'Montserrat',sans-serif;font-size:20px;line-height:26px;color:#333}

/* team */
.team{top:1245px;left:0;width:1200px;height:1345px;background:var(--grey-bg)}
.lead-photo{left:111px;top:163px;width:383px;height:393px;border-radius:0 0 0 60px;background:radial-gradient(circle at 55% 45%,#e6b79b 0%,#c78556 40%,#8c4f26 100%)}
.lead-name{left:557px;top:160px;font-family:'Montserrat',sans-serif;font-size:35px;font-weight:500}
.role{font-family:'Montserrat',sans-serif;color:var(--orange);font-weight:500}
.lead-role{left:557px;top:210px;font-size:24px}
.lead-copy{left:557px;top:262px;width:525px;font-size:15px;line-height:26.5px;color:var(--body)}
.lead-btn{left:559px;top:477px;width:190px;height:55px;font-size:15px}
.social{display:flex;gap:12px}
.social span{width:44px;height:44px;border-radius:50%;border:2px solid #555;display:flex;align-items:center;justify-content:center}
.dot{width:10px;height:10px;border-radius:2px;background:var(--orange)}
.member{width:240px;text-align:center}
.member .photo{width:228px;height:228px;border-radius:50%;margin:0 auto}
.member h3{margin-top:36px;font-family:'Montserrat',sans-serif;font-weight:500;font-size:25px}
.member .role{margin-top:12px;font-size:18px;line-height:23px}
.member .copy{margin-top:18px;font-size:15px;line-height:25px}
.member .social{justify-content:center;margin-top:20px}
.member .btn{width:158px;height:46px;font-size:13px;margin:30px auto 0}

/* testimonials */
.quote{left:170px;top:2780px;width:860px;font-style:italic;font-size:16px;line-height:28px;color:var(--body);text-align:center}
.avatar{left:542px;top:2912px;width:115px;height:115px;border-radius:50%;background:radial-gradient(circle at 50% 40%,#e8c8ad 0%,#b58a64 55%,#6d4c33 100%)}

/* partners */
.partners{top:3153px;left:0;width:1200px;height:1147px;background:var(--grey-bg)}
.badge{height:110px;border:2px solid var(--line);background:var(--white);display:flex;align-items:center;justify-content:center;gap:12px;font-family:'Montserrat',sans-serif;font-weight:600;font-size:30px;color:var(--ink)}
.badge.on{border-color:var(--orange)}
.badge i{width:18px;height:18px;border-radius:50%;background:var(--ink)}
.sub{left:0;width:1200px;text-align:center;font-family:'Montserrat',sans-serif;font-weight:500;font-size:20px;line-height:26px;color:#333}

/* contact */
.contact{top:4300px;left:0;width:1200px;height:702px;background:linear-gradient(180deg,#3a3f47 0%,#262a31 100%)}
.contact .h2{color:var(--white)}
.field{height:43px;background:var(--white);font-size:15px;color:#555;padding:13px 16px}
.label{color:var(--white);font-size:15px}
.check{display:flex;align-items:center;gap:8px;color:var(--white);font-size:15px}
.check b{width:13px;height:13px;border:1.5px solid var(--white)}
.send{left:548px;top:4873px;width:106px;height:54px;font-size:16px}

/* footer */
.footer-copy{left:111px;top:5032px;font-size:15px;color:#333}
.foot-social{left:878px;top:5018px;display:flex;gap:11px}
.foot-social span{width:44px;height:44px;border-radius:50%;border:2px solid var(--orange);display:flex;align-items:center;justify-content:center}
</style>
</head>
<body>

<!-- HERO -->
<section class="abs hero" role="img" aria-label="Conference audience photograph in dark blue tones"></section>
<div class="abs logo"><span class="mark"></span>QLV Advisors</div>
<nav class="abs nav"><span>Home</span><span>Services</span><span>Resources</span><span>Events</span><span>Blog</span><span class="active">About Us</span></nav>
<div class="abs btn nav-cta">Contact Us</div>
<h1 class="abs hero-title">ABOUT US</h1>

<!-- WHO WE ARE -->
<div class="abs eyebrow" style="top:510px">Who We Are</div>
<h2 class="abs h2" style="top:553px">About QLV Advisors</h2>
<p class="abs copy" style="left:230px;top:620px;width:740px">QLV Advisors helps event and media companies as well as the technology partners that support them modernize revenue organizations and future proof their businesses.</p>
<p class="abs copy" style="left:230px;top:699px;width:740px">We created and trademarked Harbor Ledger organizational model to help our customers achieve optimal and consistent sales acceleration and work with our clients to implement some or all of its core components depending on their unique business needs.</p>
<p class="abs copy" style="left:230px;top:805px;width:740px">We have deep expertise in the verticals we serve, and we understand the transformational shifts required to survive and thrive. Our services range from strategic consulting and interim sales leadership to satellite and full-funnel sales.</p>

<div class="abs value" style="left:89px;top:925px">
  <div class="ring"><div class="ring-in">
    <svg width="70" height="80" viewBox="0 0 70 80" fill="none" stroke="#f24f1c" stroke-width="3"><rect x="8" y="6" width="46" height="64" rx="3"/><circle cx="40" cy="22" r="9"/><path d="M36 22l3 3 6-6M18 42h28M18 50h28M18 58h20"/></svg>
  </div></div>
  <p>Total Transparency<br>Authenticity</p>
</div>
<div class="abs value" style="left:344px;top:925px">
  <div class="ring"><div class="ring-in">
    <svg width="80" height="80" viewBox="0 0 80 80" fill="none" stroke="#f24f1c" stroke-width="3"><path d="M20 10l3 6 6 1-4 4 1 6-6-3-6 3 1-6-4-4 6-1zM40 6l3 6 6 1-4 4 1 6-6-3-6 3 1-6-4-4 6-1zM60 10l3 6 6 1-4 4 1 6-6-3-6 3 1-6-4-4 6-1z"/><circle cx="38" cy="42" r="8"/><path d="M22 68c2-10 9-15 16-15s12 3 14 8"/><circle cx="56" cy="62" r="9"/><path d="M52 62l3 3 6-6"/></svg>
  </div></div>
  <p>Customer<br>Satisfaction</p>
</div>
<div class="abs value" style="left:599px;top:925px">
  <div class="ring"><div class="ring-in">
    <svg width="80" height="80" viewBox="0 0 80 80" fill="none" stroke="#f24f1c" stroke-width="3"><circle cx="40" cy="22" r="8"/><path d="M40 6v6M40 32v6M24 22h6M50 22h6M29 11l4 4M47 29l4 4M51 11l-4 4M33 29l-4 4"/><path d="M14 50l10-8 8 10v18M66 50l-10-8-8 10v18M34 58v12M40 56v14M46 58v12"/></svg>
  </div></div>
  <p>Extreme Ownership<br>&amp; Accountability</p>
</div>
<div class="abs value" style="left:856px;top:925px">
  <div class="ring"><div class="ring-in">
    <svg width="80" height="80" viewBox="0 0 80 80" fill="none" stroke="#f24f1c" stroke-width="3"><path d="M40 40C28 30 22 24 22 16a9 9 0 0118-2 9 9 0 0118 2c0 8-6 14-18 24z"/><path d="M10 56l12-6c6-3 12-2 16 2h12a4 4 0 010 8H36M50 58l14-8a4 4 0 014 6L48 70H26l-8 4"/></svg>
  </div></div>
  <p>Passion for<br>Everthing we do</p>
</div>

<!-- TEAM -->
<section class="abs team">
  <h2 class="abs h2" style="top:60px">Our Team</h2>
  <div class="abs lead-photo" role="img" aria-label="Portrait photo of the founder and managing partner"></div>
  <div class="abs lead-name">Marisa L. Vantrell-Oakes</div>
  <div class="abs role lead-role">Founder &amp; Managing Partner</div>
  <p class="abs lead-copy">What I do: I run all aspects of the business including working directly with each client to drive growth, innovation and new business models. A top performing multi-functional executive in the events, media and event tech industries, I am passionate about all things related to sales, revenue stream innovation, &amp; new organizational structures. I am particularly adept at helping my clients achieve growth during challenging times.</p>
  <div class="abs btn lead-btn">More About Me</div>
  <div class="abs social" style="left:986px;top:483px">
    <span aria-label="Email"><svg width="18" height="14" viewBox="0 0 18 14"><rect width="18" height="14" rx="2" fill="#f24f1c"/><path d="M1 2l8 6 8-6" stroke="#fff" stroke-width="1.5" fill="none"/></svg></span>
    <span aria-label="Professional profile"><i class="dot"></i></span>
  </div>

  <div class="abs member" style="left:103px;top:631px">
    <div class="photo" role="img" aria-label="Portrait photo of the vice president" style="background:radial-gradient(circle at 50% 40%,#f0d6c0 0%,#c9a07a 45%,#8a5a3a 100%)"></div>
    <h3>Nora Pellham</h3>
    <div class="role">Vice President<br>Business Development</div>
    <p class="copy">What I do: I lead QLV’s business development efforts, support our client’s sales needs, and provide guidance on “outside the square foot” revenue strategies</p>
    <div class="social"><span><svg width="18" height="14" viewBox="0 0 18 14"><rect width="18" height="14" rx="2" fill="#f24f1c"/><path d="M1 2l8 6 8-6" stroke="#fff" stroke-width="1.5" fill="none"/></svg></span><span><i class="dot"></i></span></div>
    <div class="btn">More About Me</div>
  </div>
  <div class="abs member" style="left:354px;top:631px">
    <div class="photo" role="img" aria-label="Portrait photo of the account executive" style="background:radial-gradient(circle at 50% 45%,#c9a183 0%,#6e5140 50%,#2b211b 100%)"></div>
    <h3>Dev Halloran</h3>
    <div class="role">Account<br>Executive</div>
    <p class="copy">What I do: I help fulfill our clients’ needs and ensure that they have consistent growth using highly targeted marketing, prospecting, and lead generation.</p>
    <div class="social"><span><svg width="18" height="14" viewBox="0 0 18 14"><rect width="18" height="14" rx="2" fill="#f24f1c"/><path d="M1 2l8 6 8-6" stroke="#fff" stroke-width="1.5" fill="none"/></svg></span><span><i class="dot"></i></span></div>
    <div class="btn">More About Me</div>
  </div>
  <div class="abs member" style="left:604px;top:631px">
    <div class="photo" role="img" aria-label="Portrait photo of the marketing director" style="background:radial-gradient(circle at 50% 40%,#e9cdb2 0%,#a88a60 45%,#55603a 100%)"></div>
    <h3>Lucia Ferrante</h3>
    <div class="role">Director of Marketing &amp;<br>Program Management</div>
    <p class="copy">What I do: I handle marketing, database development, and am actively working on launching a new QLV service that connects influencers to our customers.</p>
    <div class="social"><span><svg width="18" height="14" viewBox="0 0 18 14"><rect width="18" height="14" rx="2" fill="#f24f1c"/><path d="M1 2l8 6 8-6" stroke="#fff" stroke-width="1.5" fill="none"/></svg></span><span><i class="dot"></i></span></div>
    <div class="btn">More About Me</div>
  </div>
  <div class="abs member" style="left:853px;top:631px">
    <div class="photo" role="img" aria-label="Portrait photo of the market development assistant" style="background:radial-gradient(circle at 50% 40%,#f1d9c6 0%,#b79a84 45%,#7d8a8e 100%)"></div>
    <h3>Jenna Marlow</h3>
    <div class="role">Market Development<br>Assistant</div>
    <p class="copy">What I do: I support both the marketing and sales functions of QLV Advisors by assisting in sales prospecting, producing social media content, and conducting research</p>
    <div class="social"><span><svg width="18" height="14" viewBox="0 0 18 14"><rect width="18" height="14" rx="2" fill="#f24f1c"/><path d="M1 2l8 6 8-6" stroke="#fff" stroke-width="1.5" fill="none"/></svg></span><span><i class="dot"></i></span></div>
    <div class="btn">More About Me</div>
  </div>
</section>

<!-- TESTIMONIALS -->
<div class="abs eyebrow" style="top:2666px">Reviews</div>
<h2 class="abs h2" style="top:2706px">Client Testimonials</h2>
<svg class="abs" style="left:110px;top:2820px" width="22" height="36" viewBox="0 0 22 36"><path d="M18 3L4 18l14 15" stroke="#555" stroke-width="3" fill="none"/></svg>
<svg class="abs" style="left:1068px;top:2820px" width="22" height="36" viewBox="0 0 22 36"><path d="M4 3l14 15L4 33" stroke="#555" stroke-width="3" fill="none"/></svg>
<p class="abs quote">“ Marisa worked with Kindrel for 16 months, helping to build and strengthen our profile in the US. She showed us how we could better expand our business, taught us fundamental sales practice and helped to identify where our product gaps were. Marisa’s single minded determination to achieve her goals is extraordinary and she will be a passionate and credible champion for any business that she chooses to work with. ”</p>
<div class="abs avatar" role="img" aria-label="Portrait photo of the reviewer"></div>
<div class="abs center" style="left:0;top:3044px;width:1200px;font-family:'Montserrat',sans-serif;font-weight:600;font-size:15px">ILANA MOSS</div>
<div class="abs center" style="left:0;top:3067px;width:1200px;font-size:15px;color:var(--body)">CEO / Kindrel</div>

<!-- PARTNERS -->
<section class="abs partners">
  <h2 class="abs h2" style="top:60px">Partners</h2>
  <div class="abs eyebrow" style="top:128px;font-size:21px">Current</div>
  <div class="abs badge" style="left:158px;top:176px;width:220px">Vexbyte Live</div>
  <div class="abs badge on" style="left:494px;top:176px;width:220px"><i></i>Tandril</div>
  <div class="abs badge" style="left:830px;top:176px;width:220px">Corvath</div>
  <div class="abs sub" style="top:320px">Event technology platform</div>
  <p class="abs copy" style="left:340px;top:362px;width:520px;font-size:15px;line-height:25px">Tandril is built to foster meaningful engagement and interactions between event participants. From easy-to-watch content to AI powered matchmaking and the scheduling of 1:1 meetings, events using Tandril offer high touch engagement, deliver enhanced ROI to sponsors and attendees, and benefit from improved retention and customer satisfaction. QLV Advisors is the sales arm for Tandril in North and South America.</p>
  <div class="abs eyebrow" style="top:591px;font-size:21px">Past</div>
  <div class="abs badge" style="left:113px;top:639px;width:219px"><i></i>Kindrel</div>
  <div class="abs badge" style="left:366px;top:639px;width:219px">Plumeo</div>
  <div class="abs badge" style="left:619px;top:639px;width:217px;color:var(--orange)">Keystreet</div>
  <div class="abs badge" style="left:870px;top:639px;width:219px">Brackwell</div>
  <div class="abs sub" style="top:782px">Integrated B2B media and events organization<br>focused on the Commercial Real Estate industry</div>
  <p class="abs copy" style="left:340px;top:858px;width:520px;font-size:15px;line-height:25px">Keystreet, based out of NYC, is an integrated media portfolio of digital media and live event solutions focused on the Commercial Real Estate industry. Our consulting project focused on evaluating the entire scope of the business to improve customer satisfaction to drive revenue growth in the areas of attendee ticket sales and event sponsorship. Key areas of focus included identifying onsite audience experience improvements, connecting the dots between digital content and live event content and identifying new revenue opportunities to expand customer value delivery.</p>
</section>

<!-- CONTACT -->
<section class="abs contact" role="img" aria-label="Dark tinted photo of business charts on a desk">
  <div class="abs eyebrow" style="top:68px">Get In Touch</div>
  <h2 class="abs h2" style="top:108px">Contact Us</h2>
</section>
<div class="abs field" style="left:168px;top:4490px;width:283px">First Name</div>
<div class="abs field" style="left:461px;top:4490px;width:280px">Last Name</div>
<div class="abs field" style="left:751px;top:4490px;width:281px">Email Address</div>
<div class="abs field" style="left:168px;top:4547px;width:283px">Job Title</div>
<div class="abs field" style="left:461px;top:4547px;width:280px">Company Name</div>
<div class="abs field" style="left:751px;top:4547px;width:281px">Phone No</div>
<div class="abs label" style="left:168px;top:4609px">How can we help you?</div>
<div class="abs check" style="left:170px;top:4645px"><b></b>Harbor Ledger™</div>
<div class="abs check" style="left:377px;top:4645px"><b></b>Sales Organization Modernization</div>
<div class="abs check" style="left:682px;top:4645px"><b></b>Digital Strategy</div>
<div class="abs check" style="left:170px;top:4682px"><b></b>Outsourced Sales</div>
<div class="abs check" style="left:377px;top:4682px"><b></b>Other</div>
<div class="abs field" style="left:168px;top:4725px;width:864px;height:113px">Message</div>
<div class="abs btn send">Send</div>

<!-- FOOTER -->
<div class="abs footer-copy">Copyright © 2021, QLV Advisors. All rights reserved.</div>
<div class="abs foot-social"><span aria-label="Social profile"><i class="dot"></i></span><span aria-label="Social profile"><i class="dot"></i></span><span aria-label="Social profile"><i class="dot"></i></span><span aria-label="Social profile"><i class="dot"></i></span></div>

</body>
</html>
```